Geschäftspapiere für Personalvermittler
Sehr Guter Disigner. Versteht alles und setzt alles schnell um. Wir danken TUVI417 für die gute Zusammenarbeit. Quandrel UG
Zielgruppe
Das Startup ist ein Experte für die Personalvermittlung von Fachkräften und Führungskräften in verschiedenen Branchen.
Neben der Rekrutierung von Fach- und Führungskräften können wir auch Softwareentwicklungsdienste anbieten.
Hallo liebe Designer,
wir freuen uns, dass Sie sich für unseren Wettbewerb interessieren.
Wir benötigen ein design für
1) Visitenkarten + QR-Code
2) Briefpappier
Folgende Informationen müssen im Geschäftspapier vorhanden sein:
Firmenname
Adresse
Tel
Fax
Internet
E-Mail
Name Bank
IBAN
BIC
Geschäftsführer
Sitz der Gesellschaft: Hamburg
Amtsgericht
Wir setzen Eurer Phantasie keine Grenzen und brauchen innovative Ideen.
Bitte verwenden Sie ein QR-Code.
Wir wünschen viel Erfolg.
Ihr Quandrel Team

```html
<!DOCTYPE html>
<html lang="de">
<head>
<meta charset="utf-8">
<title>Quandrel – Briefpapier und Umschlag</title>
<link rel="stylesheet" href="https://fonts.googleapis.com/css2?family=Montserrat:wght@500&family=PT+Sans+Narrow&family=Arimo&display=swap">
<style>
  :root{
    --stage:#4f4f4f;
    --paper:#ffffff;
    --brand-blue:#2196d3;
    --brand-orange:#f39a1e;
    --ink:#5a5a5a;
    --ink-dark:#3c3c3c;
    --rule:#a7a7a7;
  }
  *{margin:0;padding:0;box-sizing:border-box}
  html,body{width:1200px;height:1199px;overflow:hidden;background:var(--stage)}
  .canvas{position:relative;width:1200px;height:1199px}
  .letter{position:absolute;left:33px;top:91px;width:720px;height:1018px;background:var(--paper)}
  .abs{position:absolute}
  .wordmark{font-family:'Montserrat',sans-serif;font-weight:500;color:var(--brand-blue);letter-spacing:1px;white-space:nowrap;display:flex;align-items:center;gap:8px}
  .wordmark .mark{background:var(--brand-orange);display:inline-block}
  .rule{position:absolute;height:1px;background:var(--rule)}
  .info{font-family:'PT Sans Narrow',sans-serif;color:var(--ink);white-space:nowrap;display:flex;align-items:center;justify-content:flex-end;gap:6px}
  .info svg{fill:var(--ink);flex:none}
  .window-marks{position:absolute;left:89px;top:165px;width:299px;height:145px}
  .sender-line{position:absolute;left:119px;top:175px;font-family:'PT Sans Narrow',sans-serif;font-size:7px;color:var(--ink-dark);white-space:nowrap}
  .recipient{position:absolute;left:112px;top:227px;font-family:'PT Sans Narrow',sans-serif;font-size:12.5px;line-height:14.5px;color:var(--ink-dark)}
  .footer{position:absolute;left:0;width:720px;top:966px;text-align:center;font-family:'Arimo',sans-serif;font-size:8px;line-height:15px;color:var(--ink);letter-spacing:-.2px}
  .envelope{position:absolute;left:403px;top:521px;width:771px;height:385px;background:var(--paper);box-shadow:6px 8px 8px rgba(0,0,0,.45)}
  .flap{position:absolute;left:403px;top:428px}
  .env-window{position:absolute;left:56px;top:192px;width:325px;height:145px;border:1px solid #444;border-radius:22px}
</style>
</head>
<body>
<div class="canvas">

  <section class="letter" aria-label="Briefbogen">
    <div class="abs wordmark" style="left:30px;top:100px;font-size:30px">
      <span class="mark" style="width:14px;height:14px"></span>QUANDREL
    </div>
    <div class="rule" style="left:30px;top:96px;width:659px"></div>

    <div class="abs info" style="right:32px;top:80px;font-size:10.5px">
      Werftweg 9 &nbsp;•&nbsp; 24103 Kiel
      <svg width="13" height="12" viewBox="0 0 13 12"><path d="M6.5 0 13 6h-2v6H8V8H5v4H2V6H0z"/></svg>
    </div>
    <div class="abs info" style="right:32px;top:106px;font-size:10px;flex-direction:column;align-items:flex-end;gap:3px">
      <div class="info">0431 552870-0
        <svg width="12" height="12" viewBox="0 0 12 12"><circle cx="6" cy="6" r="5.4" fill="none" stroke="#5a5a5a"/><path d="M4 3h1.5l.6 1.6-.9.7a4 4 0 0 0 1.6 1.6l.7-.9L9 7v1.5C6 9 3.5 6.5 4 3z"/></svg></div>
      <div class="info">0431 552870-19
        <svg width="12" height="12" viewBox="0 0 12 12"><rect x="3" y="1" width="6" height="4"/><rect x="1" y="5" width="10" height="5" rx="1"/></svg></div>
      <div class="info">0162 4471930 (nur auf VK)
        <svg width="12" height="12" viewBox="0 0 12 12"><rect x="3.5" y="1" width="5" height="10" rx="1" fill="none" stroke="#5a5a5a"/></svg></div>
      <div class="info">info@quandrel.de
        <svg width="12" height="12" viewBox="0 0 12 12"><rect x="1" y="3" width="10" height="7"/><path d="M1 3l5 4 5-4" fill="none" stroke="#fff"/></svg></div>
    </div>

    <svg class="window-marks" viewBox="0 0 299 145" fill="none" stroke="#555" stroke-width="1">
      <path d="M0 28V14Q0 0 14 0h12"/><path d="M273 0h12q14 0 14 14v14"/>
      <path d="M0 117v14q0 14 14 14h12"/><path d="M273 145h12q14 0 14-14v-14"/>
    </svg>
    <div class="sender-line">Nordkai Immobilienverwaltung GmbH • Werftweg 9 • 24103 Kiel</div>
    <div class="recipient">Herr.:<br>Henrik Maalberg<br>Web Master<br>City</div>

    <div class="footer">
      Bankverbindung: &nbsp; Förde Bank AG • IBAN: DE41 2105 0170 0093 4412 07 &nbsp;• BIC: FOBKDE21KIE<br>
      USt.IDNr.: DE318874260 • Steuernummer: 20 117 48305 &nbsp;• Amtsgericht Kiel, HRB 4718 KI
    </div>
  </section>

  <svg class="flap" width="775" height="95" viewBox="0 0 775 95" aria-hidden="true">
    <path d="M0 93 L48 4 Q50 2 54 2 H688 Q700 2 710 10 Q724 22 771 93 Z" fill="#fff"/>
  </svg>

  <section class="envelope" aria-label="Fensterumschlag">
    <div class="env-window"></div>
    <div class="rule" style="left:405px;top:276px;width:366px"></div>
    <div class="abs wordmark" style="left:405px;top:283px;font-size:21px;gap:6px">
      <span class="mark" style="width:10px;height:10px"></span>QUANDREL
    </div>
    <div class="abs info" style="left:558px;top:289px;font-size:12px;justify-content:flex-start">
      Werftweg 9 &nbsp;•&nbsp; 24103 Kiel
      <svg width="16" height="15" viewBox="0 0 13 12"><path d="M6.5 0 13 6h-2v6H8V8H5v4H2V6H0z"/></svg>
    </div>
  </section>

</div>
</body>
</html>
```